Builders Worksite Corflute Outdoor Sign

We are a building company who are just branching out into new construction. How first new build is our own home which was designed by us and a local architect. We are proud and want to create more advertisement around our business.

We need a corflute sign that can staked outside the construction site and can be seen by people passing by.
Updates

Can we please make the company name and logo bigger (Tidewater Ridge Homes) This needs to be the focus. Can we please replace 'Manu' with 'Contact Us on 021-574-3619'

Target Market(s)

Home owners and people wishing to build on lifestyle blocks in New Zealand.

Font styles to use
Sans Serif

Requirements
Must have
• It needs to feature our:
Logo
Company name
Contact name and number - Manu - 0215743619
Landscape NOT portrait.

```html
<!DOCTYPE html>
<html lang="en">
<head>
<meta charset="utf-8">
<title>Tidewater Ridge Homes – Site Sign</title>
<link href="https://fonts.googleapis.com/css2?family=Jost:wght@400&family=Montserrat:wght@800&display=swap" rel="stylesheet">
<style>
  :root {
    --backdrop: #58585a;
    --sign-white: #ffffff;
    --navy: #161d2c;
    --gold-top: #f6c51a;
    --gold-bottom: #d9a92c;
  }
  html, body {
    margin: 0;
    padding: 0;
    width: 785px;
    height: 1200px;
    overflow: hidden;
    background: var(--backdrop);
  }
  .sign {
    position: absolute;
    left: 40px;
    top: 328px;
    width: 704px;
    height: 544px;
    background: var(--sign-white);
    box-shadow: 4px 5px 8px rgba(0,0,0,0.45);
    overflow: hidden;
  }
  .sign-art {
    position: absolute;
    inset: 0;
    display: block;
  }
  .brand-name {
    font-family: "Jost", sans-serif;
    font-weight: 400;
    fill: var(--gold-top);
  }
  .contact-label,
  .contact-number {
    font-family: "Montserrat", sans-serif;
    font-weight: 800;
    fill: var(--navy);
  }
</style>
</head>
<body>
  <div class="sign">
    <svg class="sign-art" viewBox="0 0 704 544" width="704" height="544" xmlns="http://www.w3.org/2000/svg">
      <defs>
        <linearGradient id="gold-band" x1="0" y1="0" x2="0" y2="1">
          <stop offset="0" stop-color="#f6c51a"/>
          <stop offset="1" stop-color="#d9a92c"/>
        </linearGradient>
      </defs>

      <!-- roof gable -->
      <polygon class="roof" points="352,0 664,336 40,336" fill="#161d2c"/>
      <rect class="roof-base" x="0" y="336" width="704" height="14" fill="#161d2c"/>

      <!-- brand -->
      <circle class="brand-dot" cx="352" cy="162" r="50" fill="#f6c51a"/>
      <text class="brand-name" x="352" y="270" text-anchor="middle" font-size="48" textLength="418" lengthAdjust="spacingAndGlyphs">TIDEWATER RIDGE</text>
      <text class="brand-name" x="352" y="316" text-anchor="middle" font-size="30" letter-spacing="11">HOMES</text>

      <!-- contact band -->
      <rect class="contact-band" x="0" y="350" width="704" height="194" fill="url(#gold-band)"/>
      <line class="rule" x1="40" y1="394" x2="176" y2="394" stroke="#161d2c" stroke-width="4"/>
      <line class="rule" x1="528" y1="394" x2="664" y2="394" stroke="#161d2c" stroke-width="4"/>
      <text class="contact-label" x="352" y="406" text-anchor="middle" font-size="32" textLength="332" lengthAdjust="spacingAndGlyphs">CONTACT US ON</text>
      <text class="contact-number" x="352" y="500" text-anchor="middle" font-size="78" textLength="608" lengthAdjust="spacingAndGlyphs">021-574-3619</text>
    </svg>
  </div>
</body>
</html>
```